Morden, Creative, Unique, Independent Wine Shop

1. We are a brand new wine shop located in Melbourne Australia, we have our logo already, simply use the logo to design a business card.
2. I have uploaded our logo in two versions, with or without shadow, any of them is acceptable.
3. Make it as creative and unique as possible, no limitation of shape, color combination, geometry pattern, fonts, composing etc.
3. Info on the card:
- Brambleford Wine Cellar (Not very necessary if logo is obviously shown)
- 42 Carrow Steet, Wexbury, Eastmere, Australia 3472
- +61 3 9418 7360
- www.bramblefordwinecellar.example.au
- bramblefordwinecellar@mailbox.example
- Additional icons: Google, Instagram, Facebook, Twitter
4. Once again, forget it is a commercial card, make it special.

```html
<!DOCTYPE html>
<html lang="en">
<head>
<meta charset="utf-8">
<title>Brambleford Wine Cellar — Business Card</title>
<link href="https://fonts.googleapis.com/css2?family=Arimo:wght@400;700&display=swap" rel="stylesheet">
<style>
  :root {
    --backdrop: #8f8f8f;
    --card: #ffffff;
    --wine: #a3123f;
    --ink: #5a5a5a;
    --charcoal: #4b4b4b;
    --shadow: rgba(0, 0, 0, 0.35);
  }
  * { box-sizing: border-box; margin: 0; padding: 0; }
  html, body {
    width: 1200px;
    height: 960px;
    overflow: hidden;
    background: var(--backdrop);
    font-family: "Arimo", Arial, sans-serif;
  }
  .stage {
    position: relative;
    width: 1200px;
    height: 960px;
  }
  .card {
    position: absolute;
    left: 250px;
    width: 700px;
    height: 400px;
    background: var(--card);
    border-radius: 28px;
    box-shadow: 0 10px 24px var(--shadow);
    overflow: hidden;
  }
  .card--front { top: 50px; }
  .card--back { top: 510px; }

  /* Front */
  .brand {
    position: absolute;
    display: flex;
    align-items: center;
    gap: 14px;
    color: var(--wine);
    font-weight: 400;
    letter-spacing: 0.04em;
    white-space: nowrap;
  }
  .card--front .brand {
    left: 0;
    right: 0;
    top: 0;
    bottom: 0;
    justify-content: center;
    font-size: 34px;
  }
  .brand__dot {
    width: 16px;
    height: 16px;
    border-radius: 50%;
    background: var(--wine);
    flex: none;
  }

  /* Back */
  .mascot-area {
    position: absolute;
    left: 40px;
    top: 70px;
    width: 290px;
    height: 330px;
    border-radius: 140px 140px 0 0;
    background: linear-gradient(160deg, #c23a63 0%, #8a8a8a 40%, #5c5c5c 100%);
    opacity: 0.85;
  }
  .card--back .brand {
    left: 370px;
    top: 60px;
    font-size: 26px;
  }
  .person {
    position: absolute;
    left: 370px;
    top: 130px;
  }
  .person__name {
    color: var(--wine);
    font-weight: 700;
    font-size: 22px;
    letter-spacing: 0.01em;
  }
  .person__role {
    color: var(--ink);
    font-weight: 700;
    font-size: 15px;
    margin-top: 3px;
  }
  .address {
    position: absolute;
    left: 370px;
    top: 200px;
    color: var(--ink);
    font-size: 15px;
    line-height: 1.35;
  }
  .contacts {
    position: absolute;
    left: 370px;
    top: 258px;
    list-style: none;
    color: var(--ink);
    font-size: 15px;
  }
  .contacts li {
    display: flex;
    align-items: center;
    gap: 10px;
    line-height: 1.45;
    white-space: nowrap;
  }
  .contacts svg {
    width: 13px;
    height: 13px;
    fill: var(--wine);
    flex: none;
  }
</style>
</head>
<body>
<main class="stage">
  <section class="card card--front" aria-label="Card front">
    <div class="brand">
      <span class="brand__dot"></span>
      <span class="brand__name">Brambleford Wine Cellar</span>
    </div>
  </section>

  <section class="card card--back" aria-label="Card back">
    <div class="mascot-area" role="img" aria-label="Large crowned owl mascot illustration in charcoal and wine red"></div>

    <div class="brand">
      <span class="brand__name">Brambleford Wine Cellar</span>
    </div>

    <div class="person">
      <p class="person__name">DANIEL HARROW</p>
      <p class="person__role">President</p>
    </div>

    <p class="address">42 Carrow Steet, Wexbury<br>Eastmere, Australia 3472</p>

    <ul class="contacts">
      <li>
        <svg viewBox="0 0 16 16" aria-hidden="true"><path d="M3.6 1.2l2.3 2.9-1.3 1.6c.9 2 2.7 3.8 4.7 4.7l1.6-1.3 2.9 2.3-1.3 2.2C7.4 13.8 2.2 8.6 1.4 2.5z"/></svg>
        <span>+61 3 9418 7360</span>
      </li>
      <li>
        <svg viewBox="0 0 16 16" aria-hidden="true"><path d="M1 3h14v10H1z M1.8 3.6L8 8.6l6.2-5z" fill-rule="evenodd"/></svg>
        <span>bramblefordwinecellar@mailbox.example</span>
      </li>
      <li>
        <svg viewBox="0 0 16 16" aria-hidden="true"><circle cx="8" cy="8" r="7"/></svg>
        <span>www.bramblefordwinecellar.example.au</span>
      </li>
    </ul>
  </section>
</main>
</body>
</html>
```